Computer repair services flyer

This flyer / leaflet is required to promote my local computer and laptop repair business. It will primarily be used for pinning to notice boards when I get access to shared accommodation but I will also use it in the future for posting through letterboxes in affluent areas.

Company branding, logo, services, pricing, contact details etc. can be found on my website at : www.brightlanetech.co.uk

The services I would predominantly like to promote on this flyer are :

Speeding up slow / old computers
Virus removal
Lost data recovered
Broken laptop screen replacements
Dead laptops fixed
We buy and recycle broken laptops for cash

Other features to highlight :

Friendly and experienced
We are local (Near to Cardiff city center)
Quick repair turnaround - most repairs within 24hours
Affordable / No VAT
Free diagnostics
No Fix = No fee
Free collection and delivery
We Guarantee our work

Calls to action and attention grabbing if possible. Offer 10% off. Free cooling fan clean.

Size of flyer = A5 (210 x 148mm or 8.3 x 5.8in) portrait, single sided colour.

Target Market(s)

18 to 60 years

Industry/Entity Type

Accommodation

Requirements
Must have
• 02940 613857

```html
<!DOCTYPE html>
<html lang="en">
<head>
<meta charset="utf-8">
<title>Bright Lane Tech – Computer Repair Flyer</title>
<link rel="stylesheet" href="https://fonts.googleapis.com/css2?family=Oswald:wght@400;500;600;700&display=swap">
<style>
  :root {
    --orange: #f47a1f;
    --orange-soft: #f9a25c;
    --ink: #1a1a1a;
    --grey: #444444;
    --paper: #ffffff;
  }
  * { margin: 0; padding: 0; box-sizing: border-box; }
  html, body { width: 847px; height: 1200px; overflow: hidden; background: var(--paper); }
  .flyer {
    position: relative;
    width: 847px;
    height: 1200px;
    overflow: hidden;
    font-family: "Oswald", "Arial Narrow", sans-serif;
    color: var(--ink);
    background: var(--paper);
  }
  .brand-name {
    position: absolute;
    top: 46px; left: 0; width: 100%;
    text-align: center;
    font-size: 116px;
    font-weight: 700;
    line-height: 1;
    letter-spacing: -2px;
    color: var(--ink);
  }
  .brand-tagline {
    position: absolute;
    top: 200px; left: 0; width: 100%;
    text-align: center;
    font-size: 48px;
    font-weight: 500;
    line-height: 1.2;
    color: var(--ink);
  }
  .call {
    position: absolute;
    top: 352px; left: 0; width: 100%;
    text-align: center;
    color: var(--orange);
    font-weight: 700;
  }
  .call-label { font-size: 40px; line-height: 1.25; }
  .call-number { font-size: 44px; line-height: 1.3; }

  .feature-badge {
    position: absolute;
    left: 48px;
    width: 94px; height: 94px;
    border-radius: 50%;
    background: var(--orange);
    color: var(--paper);
    font-size: 29px;
    font-weight: 600;
    display: flex; align-items: center; justify-content: center;
  }
  .badge-fast { top: 476px; }
  .badge-free { top: 626px; }
  .badge-repair { top: 768px; }

  .feature-text {
    position: absolute;
    left: 254px;
    color: var(--grey);
    font-size: 28px;
    font-weight: 500;
    line-height: 37px;
  }
  .feature-text strong { font-size: 38px; font-weight: 600; }
  .text-fast { top: 464px; font-size: 29px; }
  .text-free { top: 642px; }
  .text-repair { top: 758px; }

  .guarantee {
    position: absolute;
    top: 580px; left: 424px;
    width: 423px; height: 57px;
    background: var(--orange);
    color: var(--paper);
    font-size: 30px;
    font-weight: 600;
    display: flex; align-items: center; padding-left: 40px;
  }
  .local-note {
    position: absolute;
    top: 906px; left: 0; width: 100%;
    text-align: center;
    color: var(--orange);
    font-size: 27px;
    font-weight: 600;
    line-height: 1.3;
  }
  .offer-band {
    position: absolute;
    top: 977px; left: 0;
    width: 847px; height: 223px;
    background: var(--orange-soft);
  }
  .offer-box {
    position: absolute;
    top: 996px; left: 20px;
    width: 807px; height: 204px;
    background: var(--orange);
    color: var(--paper);
    text-align: center;
    font-weight: 600;
    padding-top: 12px;
  }
  .offer-line { font-size: 56px; line-height: 80px; }
  .offer-line .big { font-size: 82px; font-weight: 700; }
</style>
</head>
<body>
<main class="flyer">
  <h1 class="brand-name">Bright Lane Tech</h1>
  <p class="brand-tagline">We fix your PC and your laptop too!</p>

  <section class="call">
    <p class="call-label">Call Now</p>
    <p class="call-number">02940 613857 No Fix = No Fee</p>
  </section>

  <div class="feature-badge badge-fast">Fast</div>
  <p class="feature-text text-fast">Quick repair turnaround Most repairs within<br><strong>24hours</strong></p>

  <div class="guarantee">We Guarantee our work</div>

  <div class="feature-badge badge-free">Free</div>
  <p class="feature-text text-free">Affordable / No VAT<br><strong>Free</strong> diagnostics • <strong>Free</strong> collection and delivery</p>

  <div class="feature-badge badge-repair">Repair</div>
  <p class="feature-text text-repair">Speeding up slow / old computers • Virus removal<br>• Lost data recovered • Broken laptop screen<br>replacements • Dead laptops fixed<br>Buy and recycle broken laptops for cash</p>

  <p class="local-note">Friendly and experienced &nbsp;• &nbsp;We are local near to Cardiff city center</p>

  <div class="offer-band"></div>
  <section class="offer-box">
    <p class="offer-line">Calls to action !! Offer <span class="big">10%</span> off</p>
    <p class="offer-line">Free cooling fan clean</p>
  </section>
</main>
</body>
</html>
```